Kestrel Airfields Homepage Design Update

here's the current site - http://kestrelairfields-demo.net/

client is not happy with overall look.

keeping the same info - intro text, headlines, featured media excepts and general navigation options - can you come up with a nicer, slicker look for this homepage?

UPDATE: since it was asked by designer.. the general layout doesnt have to be the same. its not required to have a big image, with text below that and then smaller images/text below that. as long as we have the same content on the page, it can organized and designed in any way,

client like big images, so one way or the other, keep that... but feel free to reorganize content, explore different ways of framing it, and/or anything else. make this homepage pop!

for the designer that wins this, we'll start an additional project to update the interior.

let me know if any questions..

thanks!

tomas

Target Market(s)

aviation industry professionals, local governments, general public

Number of Pages Required

1 page

Font styles to use
Sans Serif

Requirements
Must have
• big image somewhere. same content as on current site, just designed differently.

```html
<!DOCTYPE html>
<html lang="en">
<head>
<meta charset="utf-8">
<title>Kestrel Airfields — Home</title>
<link rel="stylesheet" href="https://fonts.googleapis.com/css2?family=Open+Sans:wght@400;600;700&family=Arimo:wght@400;700&display=swap">
<style>
  :root {
    --blue: #0b6fce;
    --navy: #1b2340;
    --ink: #222;
    --grey-bg: #ebebeb;
    --footer-bg: #efefef;
    --rule: #555;
    --accent: #d2401e;
    --yellow: #ffe100;
    --white: #fff;
  }
  * { box-sizing: border-box; margin: 0; padding: 0; }
  html, body { width: 771px; height: 1200px; overflow: hidden; }
  body { position: relative; background: var(--blue); font-family: "Open Sans", Arial, sans-serif; color: var(--ink); }
  .abs { position: absolute; }

  .top-band { left: 0; top: 0; width: 771px; height: 155px; background: var(--grey-bg); }
  .side-photo { top: 155px; height: 590px; }
  .side-photo.left {
    left: 0; width: 80px;
    background:
      radial-gradient(ellipse 60px 40px at 20% 12%, rgba(255,255,255,.85), transparent 70%),
      radial-gradient(ellipse 70px 50px at 60% 30%, rgba(255,255,255,.6), transparent 70%),
      radial-gradient(ellipse 80px 60px at 30% 55%, rgba(240,246,252,.7), transparent 70%),
      radial-gradient(ellipse 70px 50px at 70% 80%, rgba(230,240,250,.6), transparent 70%),
      linear-gradient(180deg, #d2d2d2 0%, #a9a9a9 30%, #b7c8da 45%, #8db0d4 70%, #6c9acb 100%);
  }
  .side-photo.right {
    left: 673px; width: 98px;
    background:
      linear-gradient(160deg, transparent 2%, rgba(255,255,255,.9) 8%, #d8d8d8 15%, transparent 22%),
      radial-gradient(ellipse 70px 40px at 60% 22%, rgba(255,255,255,.8), transparent 70%),
      radial-gradient(ellipse 90px 60px at 40% 55%, rgba(245,249,253,.8), transparent 70%),
      radial-gradient(ellipse 80px 50px at 70% 85%, rgba(235,242,250,.7), transparent 70%),
      linear-gradient(180deg, #c9c9c9 0%, #9e9e9e 35%, #bccde0 48%, #9ab9da 72%, #7aa5d2 100%);
  }
  .band-rule { left: 0; top: 396px; width: 771px; height: 3px; background: var(--blue); }

  .brand { left: 120px; top: 54px; display: flex; align-items: center; gap: 8px; }
  .brand-dot { width: 12px; height: 12px; border-radius: 50%; background: var(--navy); }
  .brand-name { font-size: 15px; font-weight: 400; color: var(--navy); letter-spacing: .8px; }
  .top-links { top: 62px; font-size: 11px; color: var(--ink); }
  .top-links.contact { left: 535px; }
  .top-links.services { left: 614px; }

  .nav { left: 80px; top: 95px; width: 593px; height: 61px; background: var(--blue); border-radius: 12px 12px 0 0; }
  .nav-item { position: absolute; top: 0; height: 61px; display: flex; flex-direction: column; align-items: center; justify-content: flex-end; padding-bottom: 6px; color: var(--white); font-size: 11px; font-weight: 600; width: 100px; margin-left: -50px; letter-spacing: -.2px; }
  .nav-item svg { width: 26px; height: 26px; margin-bottom: 3px; }

  .hero {
    left: 80px; top: 156px; width: 593px; height: 240px;
    background:
      radial-gradient(ellipse 260px 70px at 50% 58%, rgba(40,40,40,.55), transparent 75%),
      radial-gradient(ellipse 120px 110px at 62% 35%, rgba(255,255,255,.8), transparent 70%),
      linear-gradient(180deg, transparent 68%, #2b2b2b 78%, #4a4a4a 84%, #c9c9c9 90%, #6b6b6b 100%),
      linear-gradient(180deg, #f4f4f4 0%, #e2e2e2 40%, #b9b9b9 68%, #8f8f8f 100%);
  }
  .hero-title { left: 204px; top: 207px; display: flex; align-items: flex-start; font-family: Arimo, Arial, sans-serif; color: #111; }
  .hero-title .initial { font-size: 58px; font-weight: 700; line-height: 46px; margin-right: 2px; letter-spacing: -2px; }
  .hero-title .line1 { font-size: 14.5px; letter-spacing: .4px; line-height: 17px; margin-top: 2px; }
  .hero-title .line2 { font-size: 7.2px; letter-spacing: .8px; line-height: 11px; }

  .panel { left: 80px; top: 399px; width: 593px; height: 731px; background: var(--white); border-radius: 0 0 12px 12px; }
  .intro-icon { left: 348px; top: 440px; }
  .intro-head { left: 80px; top: 499px; width: 593px; text-align: center; font-family: Arimo, Arial, sans-serif; font-size: 11px; font-weight: 700; letter-spacing: .3px; line-height: 18px; color: var(--navy); }
  .intro-rule { left: 245px; top: 552px; width: 258px; height: 1px; background: var(--rule); }
  .intro-copy { left: 132px; top: 579px; width: 492px; font-family: Arimo, Arial, sans-serif; font-size: 8.2px; letter-spacing: 1px; line-height: 13.4px; color: var(--ink); text-align: justify; }
  .read-more { left: 567px; top: 670px; font-size: 11px; color: var(--accent); letter-spacing: .3px; }

  .media-rule-short { left: 312px; width: 124px; height: 1px; background: var(--rule); }
  .media-rule-long { left: 80px; top: 745px; width: 593px; height: 1px; background: #9a9a9a; }
  .media-label { left: 306px; top: 736px; padding: 0 4px; background: var(--white); font-family: Arimo, Arial, sans-serif; font-size: 10px; letter-spacing: 1.3px; color: #333; }
  .media-label .q { color: var(--accent); font-weight: 700; font-size: 12px; }

  .media-card { top: 802px; width: 170px; text-align: center; }
  .media-photo { width: 106px; height: 106px; border-radius: 50%; border: 2px solid var(--blue); margin: 0 auto 10px; }
  .media-title { font-size: 9.5px; font-weight: 600; color: #111; line-height: 12px; }
  .media-sub { font-size: 6.6px; color: #222; line-height: 8px; }
  .media-date { font-size: 6.6px; color: var(--blue); margin-top: 9px; }
  .arrow { top: 850px; }

  .footer { left: 80px; top: 1008px; width: 593px; height: 122px; background: var(--footer-bg); border-radius: 0 0 12px 12px; }
  .footer-rule { top: 1007px; height: 1px; width: 108px; background: #777; }
  .footer-menu-btn { left: 371px; top: 990px; }
  .footer-head { top: 1052px; font-family: Arimo, Arial, sans-serif; font-size: 8px; font-weight: 700; color: #111; letter-spacing: .3px; }
  .footer-list { top: 1072px; list-style: none; font-family: Arimo, Arial, sans-serif; font-size: 6px; line-height: 10.2px; color: #333; letter-spacing: .3px; }
</style>
</head>
<body>
  <div class="abs top-band"></div>
  <div class="abs side-photo left" role="img" aria-label="Soft grey sky with clouds"></div>
  <div class="abs side-photo right" role="img" aria-label="Aircraft wing above the clouds"></div>
  <div class="abs band-rule"></div>

  <header>
    <div class="abs brand"><span class="brand-dot"></span><span class="brand-name">kestrel airfields</span></div>
    <a class="abs top-links contact">contact us</a>
    <a class="abs top-links services">services</a>
  </header>

  <nav class="abs nav">
    <div class="nav-item" style="left:48px">
      <svg viewBox="0 0 26 26"><path d="M13 2 L24 12 H20 V23 H6 V12 H2 Z" fill="var(--yellow)"/><rect x="11" y="16" width="4" height="7" fill="var(--blue)"/></svg>ABOUT</div>
    <div class="nav-item" style="left:137px">
      <svg viewBox="0 0 26 26"><circle cx="13" cy="13" r="4" fill="#fff"/><g stroke="#fff" stroke-width="1.5"><line x1="13" y1="1" x2="13" y2="7"/><line x1="13" y1="19" x2="13" y2="25"/><line x1="1" y1="13" x2="7" y2="13"/><line x1="19" y1="13" x2="25" y2="13"/><line x1="4.5" y1="4.5" x2="8.5" y2="8.5"/><line x1="17.5" y1="17.5" x2="21.5" y2="21.5"/><line x1="21.5" y1="4.5" x2="17.5" y2="8.5"/><line x1="8.5" y1="17.5" x2="4.5" y2="21.5"/></g></svg>SERVICES</div>
    <div class="nav-item" style="left:228px">
      <svg viewBox="0 0 26 26"><path d="M4 14 L10 20 L23 6" fill="none" stroke="#fff" stroke-width="4"/></svg>AIRPORTS</div>
    <div class="nav-item" style="left:334px">
      <svg viewBox="0 0 26 26"><circle cx="11" cy="10" r="7" fill="none" stroke="#fff" stroke-width="2.5"/><line x1="16" y1="15" x2="23" y2="23" stroke="#fff" stroke-width="3.5"/></svg>NEWS &amp; MEDIA</div>
    <div class="nav-item" style="left:438px">
      <svg viewBox="0 0 26 26"><path d="M7 3 H19 V10 A6 6 0 0 1 7 10 Z" fill="#fff"/><path d="M7 5 H3 A4 4 0 0 0 8 12 M19 5 H23 A4 4 0 0 1 18 12" fill="none" stroke="#fff" stroke-width="1.5"/><rect x="12" y="15" width="2" height="5" fill="#fff"/><rect x="8" y="20" width="10" height="3" fill="#fff"/></svg>CONTACT US</div>
    <div class="nav-item" style="left:543px">
      <svg viewBox="0 0 26 26"><path d="M13 2 A8 8 0 0 1 18 16 V18 H8 V16 A8 8 0 0 1 13 2 Z" fill="#fff"/><rect x="9" y="19" width="8" height="2" fill="#fff"/><rect x="10" y="22" width="6" height="2" fill="#fff"/></svg>EMPLOYEES</div>
  </nav>

  <div class="abs hero" role="img" aria-label="Black and white photo of a jet airliner landing, wheels down, over hills"></div>
  <div class="abs hero-title">
    <span class="initial">B</span>
    <div><div class="line1">RINGING PRIVATE</div><div class="line2">FREE ENTERPRISE BUSINESS PRACTICES<br>TO AIRPORTS THROUGHOUT THE U.S</div></div>
  </div>

  <main>
    <div class="abs panel"></div>
    <svg class="abs intro-icon" width="42" height="40" viewBox="0 0 42 40">
      <circle cx="19" cy="21" r="16" fill="none" stroke="var(--blue)" stroke-width="2.5"/>
      <path d="M8 32 L36 5" stroke="var(--white)" stroke-width="5"/>
      <path d="M10 30 L36 5 M26 10 L34 16 M27 8 L20 4 M14 26 L17 30 M13 24 L9 23" stroke="var(--blue)" stroke-width="2.5" fill="none"/>
    </svg>
    <h1 class="abs intro-head">WE DEVELOP P3 AIRPORT OPPORTUNITIES<br>WITHIN THE U.S. MARKET</h1>
    <div class="abs intro-rule"></div>
    <p class="abs intro-copy">Kestrel Airfields is focused on opportunities to invest, develop and manage both general aviation and commercial service airports in key U.S. markets. A subsidiary of Harrier Capital Group, a private equity firm that exclusively invests in the Aerospace &amp; Transportation sectors, Kestrel has the resources available to invest and finance transactions.<br>Kestrel maintains offices in New York, Dublin and Atlanta.</p>
    <a class="abs read-more">read more</a>

    <div class="abs media-rule-short" style="top:722px"></div>
    <div class="abs media-rule-long"></div>
    <div class="abs media-label"><span class="q">❛❛</span> FEATURED MEDIA <span class="q">❜❜</span></div>
    <div class="abs media-rule-short" style="top:760px"></div>

    <svg class="abs arrow" style="left:88px" width="20" height="24" viewBox="0 0 20 24"><path d="M16 2 L5 12 L16 22" fill="none" stroke="#111" stroke-width="5"/></svg>
    <svg class="abs arrow" style="left:646px" width="20" height="24" viewBox="0 0 20 24"><path d="M4 2 L15 12 L4 22" fill="none" stroke="#111" stroke-width="5"/></svg>

    <article class="abs media-card" style="left:103px">
      <div class="media-photo" role="img" aria-label="Glass-walled passenger terminal interior" style="background:linear-gradient(180deg,#f3f5f7 0%,#dfe3e8 22%,#6f8fb4 30%,#a9c3df 45%,#4f79a8 62%,#c7a77a 78%,#5b4e44 100%)"></div>
      <div class="media-title">KESTREL AIRFIELDS</div>
      <div class="media-sub">TO DEVELOP PASSENGER<br>TERMINAL AT MARLOW FIELD</div>
      <div class="media-date">JANUARY 15, 2015</div>
    </article>
    <article class="abs media-card" style="left:292px">
      <div class="media-photo" role="img" aria-label="Airliner on a runway seen head-on" style="background:radial-gradient(ellipse 40px 16px at 50% 52%,rgba(40,40,40,.75),transparent 75%),linear-gradient(180deg,#fafafa 0%,#e4e4e4 45%,#9a9a9a 62%,#5e5e5e 78%,#b5b5b5 100%)"></div>
      <div class="media-title">PLANS FOR SECOND COMMERCIAL</div>
      <div class="media-sub">AIRPORT IN METRO-ATLANTA<br>MOVING FORWARD</div>
      <div class="media-date">MARCH 15, 2015</div>
    </article>
    <article class="abs media-card" style="left:471px">
      <div class="media-photo" role="img" aria-label="Private jet nose in dark hangar light" style="background:radial-gradient(ellipse 34px 26px at 50% 50%,#dcdcdc,#7a7a7a 55%,transparent 100%),radial-gradient(circle at 50% 15%,#6a6a6a,#1a1a1a 60%,#050505)"></div>
      <div class="media-title">KESTREL PARTICIPATES</div>
      <div class="media-sub">IN AIRPORT P3 CONGRESSIONAL<br>ROUNDTABLE</div>
      <div class="media-date">JANUARY 15, 2015</div>
    </article>
  </main>

  <footer>
    <div class="abs footer"></div>
    <div class="abs footer-rule" style="left:237px"></div>
    <div class="abs footer-rule" style="left:425px"></div>
    <svg class="abs footer-menu-btn" width="36" height="36" viewBox="0 0 36 36">
      <circle cx="18" cy="18" r="17" fill="var(--blue)" stroke="var(--white)" stroke-width="1" stroke-dasharray="2 2"/>
      <rect x="9" y="10" width="18" height="4" rx="2" fill="#fff"/><rect x="9" y="16" width="18" height="4" rx="2" fill="#fff"/><rect x="9" y="22" width="18" height="4" rx="2" fill="#fff"/>
    </svg>
    <div class="abs footer-head" style="left:189px">MENU</div>
    <div class="abs footer-head" style="left:395px">PORDUCT'S SECTORS</div>
    <ul class="abs footer-list" style="left:189px"><li>HOME</li><li>ABOUT US</li><li>BEST OFFERS</li><li>WHY US</li></ul>
    <ul class="abs footer-list" style="left:270px"><li>MEN</li><li>WOMEN</li><li>BOYS AND GIRLS</li><li>OUT OF CATEGORY</li></ul>
    <ul class="abs footer-list" style="left:395px"><li>MEN</li><li>WOMEN</li><li>BOYS AND GIRLS</li><li>OUT OF CATEGORY</li></ul>
    <ul class="abs footer-list" style="left:526px"><li>HOME</li><li>ABOUT US</li><li>BEST OFFERS</li><li>WHY US</li></ul>
  </footer>
</body>
</html>
```